Iconic Australian Wine Brand looking for a complete brand makeover

- Require a new label design for the Clover Ridge range of wines
- Complete brand makeover with refreshed packaging design
- Inspiration for consumers to see the brand in a new light
- The final design should communicate fun, energetic and modern packaging with the aim of engaging our core target market of 20 - 35 year old female wine drinkers, while re-engaging our loyal female demographic of 35+ year olds.

Target Market(s)

Engage a Core target market of 20-35 year old female wine drinkers / secondary target market: re-engage our loyal female demographic of 35+ year olds

Requirements
Must have
• Complete brand makeover in order to re-engage our loyal female drinkers, now in their mid to late 30's
Nice to have
• Play on words for the Brand name

```html
<!DOCTYPE html>
<html lang="en">
<head>
<meta charset="utf-8">
<title>Clover Ridge – Label Range</title>
<link rel="stylesheet" href="https://fonts.googleapis.com/css2?family=Ubuntu:wght@300;400&display=swap">
<style>
  :root {
    --backdrop: #d9d9db;
    --paper: #f7f5ee;
    --ink: #4a4a4a;
    --pinot: #3fb8b0;
    --shiraz: #b8326f;
    --sauvblanc: #1f6fc4;
    --cabernet: #a63fb5;
    --pinot-soft: #a9ddd7;
    --shiraz-soft: #e3aac4;
    --sauvblanc-soft: #a9c4ec;
    --cabernet-soft: #dbb2e3;
  }
  * { box-sizing: border-box; margin: 0; padding: 0; }
  html, body { width: 1200px; height: 721px; overflow: hidden; }
  body {
    background: var(--backdrop);
    font-family: "Ubuntu", sans-serif;
    color: var(--ink);
  }
  .range {
    display: flex;
    gap: 40px;
    padding: 70px 60px;
    height: 721px;
  }
  .label {
    width: 240px;
    height: 581px;
    background: var(--paper);
    box-shadow: 0 2px 10px rgba(0,0,0,0.12);
    display: flex;
    flex-direction: column;
    align-items: center;
    padding: 70px 18px 56px;
  }
  .brand-dot {
    width: 150px;
    height: 150px;
    border-radius: 50%;
    background: var(--soft);
  }
  .brand-name {
    margin-top: 46px;
    font-weight: 300;
    font-size: 44px;
    line-height: 1.05;
    letter-spacing: 2px;
    text-transform: lowercase;
    text-align: center;
    color: var(--ink);
  }
  .details {
    margin-top: auto;
    text-align: center;
    text-transform: uppercase;
    font-weight: 300;
    font-size: 13px;
    letter-spacing: 0.5px;
    line-height: 1.7;
  }
  .varietal {
    font-weight: 400;
    font-size: 17px;
    color: var(--accent);
    letter-spacing: 1px;
  }
  .label--pinot { --accent: var(--pinot); --soft: var(--pinot-soft); }
  .label--shiraz { --accent: var(--shiraz); --soft: var(--shiraz-soft); }
  .label--sauvblanc { --accent: var(--sauvblanc); --soft: var(--sauvblanc-soft); }
  .label--cabernet { --accent: var(--cabernet); --soft: var(--cabernet-soft); }
</style>
</head>
<body>
  <main class="range">
    <article class="label label--pinot">
      <div class="brand-dot"></div>
      <h2 class="brand-name">clover<br>ridge</h2>
      <div class="details">
        <p>2014 Central Victoria</p>
        <p class="varietal">Pinot Grigio</p>
        <p>Wine of Australia</p>
      </div>
    </article>
    <article class="label label--shiraz">
      <div class="brand-dot"></div>
      <h2 class="brand-name">clover<br>ridge</h2>
      <div class="details">
        <p>2014 Central Victoria</p>
        <p class="varietal">Shiraz</p>
        <p>Wine of Australia</p>
      </div>
    </article>
    <article class="label label--sauvblanc">
      <div class="brand-dot"></div>
      <h2 class="brand-name">clover<br>ridge</h2>
      <div class="details">
        <p>2014 Central Victoria</p>
        <p class="varietal">Sauvignon Blanc Semillon</p>
        <p>Wine of Australia</p>
      </div>
    </article>
    <article class="label label--cabernet">
      <div class="brand-dot"></div>
      <h2 class="brand-name">clover<br>ridge</h2>
      <div class="details">
        <p>2014 Central Victoria</p>
        <p class="varietal">Cabernet Sauvignon</p>
        <p>Wine of Australia</p>
      </div>
    </article>
  </main>
</body>
</html>
```